Ferrando Quispe Law Firm for Small and Medium Business: Website

We need a web design that includes coding for the Wix platform, for a new company based in Santiago, Chile, called Ferrando Quispe, Abogados y Consultores. The company is essentially a law firm, with additional advisory services in accounting, tax management and finance. The main target of the company are founders, CEOs or C-level executives of small or medium companies based in Chile.
The main menu of the web page must have the following tab options:
- Home - About us - Services – How we work -Blog – FAQ -Contact
Our main services are:

1.- Commercial and corporate law advisory
2.- Legal defense in civil, criminal, labor and family matters (litigation and arbitration)
3.- Bankruptcy and reorganization of companies
4.- Collection and recovery of assets
5.- Asset protection
6.- Financial and tax advice

We want to highlight the following services:

-Bankruptcy and reorganization of companies
-Judicial defense in civil matters
-Financial and tax advice

In addition to these services, the following will be offered:
-Lawyer at your home for special cases
-Half hour free consultation
-Monthly service packages

The final design should communicate confidence, business savvy and high execution standards and quality.

Target Market(s)

The main target of the company are founders, CEOs or C-level executives of small or medium companies based in Chile.

Industry/Entity Type

Legal industry

Coding

Coded - Design and coding required

Number of Pages Required

5+ page

Font styles to use
Serif

Requirements
Must have
• 1. Big banners para destacar los siguientes servicios: -Bankruptcy and reorganization of companies -Judicial defense in civil matters -Financial and tax advice 2. Call to action para agendar consulta legal. 3. Destacar los siguientes servicios: -Lawyer at your home for special cases -Half hour free consultation -Monthly service packages 3. Página para explicar cómo se cobra (precios transparentes): ver el siguiente sitio web: https://www.brindlemoorlegal.example/how 4. Links to Circlebook, Snapgallery and Linkedin 5. Connection to Whatsapp.
Should not have
• Look old fashioned

```html
<!DOCTYPE html>
<html lang="en">
<head>
<meta charset="utf-8">
<title>Ferrando Quispe, Abogados y Consultores</title>
<link href="https://fonts.googleapis.com/css2?family=Roboto:wght@400;500;700&display=swap" rel="stylesheet">
<style>
:root{
  --dark:#1d302b;
  --dark-2:#24382f;
  --gold:#ac9538;
  --gold-text:#ecd96c;
  --cream:#f3e48b;
  --ink:#1f2a26;
  --white:#ffffff;
  --card:#f2f2f0;
  --muted:#555;
}
*{box-sizing:border-box;margin:0;padding:0}
html,body{width:1200px;height:4402px;overflow:hidden}
body{font-family:'Roboto',Arial,sans-serif;color:var(--white);background:var(--dark);position:relative}
.abs{position:absolute}
a{color:inherit;text-decoration:none}

/* header */
.site-header{position:absolute;left:0;top:0;width:1200px;height:80px;background:var(--dark);}
.brand{position:absolute;left:111px;top:20px;display:flex;align-items:center;gap:10px}
.brand-mark{width:38px;height:38px;background:var(--gold)}
.brand-name{font-size:22px;color:var(--gold-text);line-height:1}
.brand-sub{font-size:8px;color:var(--gold-text);letter-spacing:1px;margin-top:3px}
.main-nav{position:absolute;right:112px;top:31px;display:flex;gap:28px;font-size:15px}
.main-nav .active{color:var(--gold-text)}

/* hero */
.hero{position:absolute;left:0;top:80px;width:1200px;height:658px}
.hero-photo{position:absolute;inset:0;background:linear-gradient(120deg,#6a5a46 0%,#b79a74 35%,#d8cbb8 55%,#8d7a63 80%,#4b4036 100%)}
.hero-dots{position:absolute;left:21px;top:305px;display:flex;flex-direction:column;gap:6px}
.hero-dots span{width:11px;height:11px;border:1.5px solid #fff;border-radius:50%}
.hero-dots span.on{background:#fff}
.hero-band{position:absolute;left:0;top:510px;width:1200px;height:148px;background:rgba(140,138,133,.92)}
.hero-title{position:absolute;left:111px;top:518px;font-size:56px;font-weight:700;letter-spacing:1px}
.hero-text{position:absolute;left:111px;top:584px;width:560px;font-size:15px;line-height:30px}
.btn{position:absolute;background:var(--cream);color:var(--ink);font-size:15px;font-weight:500;display:flex;align-items:center;justify-content:center;text-transform:uppercase}

/* about + how */
.about{position:absolute;left:0;top:738px;width:1200px;height:1183px;background:var(--dark-2)}
.about-bg{position:absolute;right:0;top:0;width:620px;height:700px;background:radial-gradient(ellipse at 60% 35%,rgba(90,110,100,.35),rgba(36,56,47,0) 70%)}
.about-photo{position:absolute;left:106px;top:84px;width:458px;height:458px;border-radius:50%;border:3px solid var(--gold-text);background:linear-gradient(135deg,#8a7a66,#c9b89e 50%,#5a4a3c)}
h2.sec-title{position:absolute;font-size:40px;font-weight:700;color:var(--gold-text);text-transform:uppercase}
.about-text{position:absolute;left:599px;top:211px;width:490px;font-size:13.5px;line-height:30px}
.work-card{position:absolute;top:692px;width:316px;height:340px;border-radius:6px}
.work-cap{position:absolute;top:1045px;width:316px;text-align:center;font-size:14px;font-weight:700;line-height:27px;text-transform:uppercase}

/* services */
.services{position:absolute;left:0;top:1921px;width:1200px;height:788px;background:var(--gold)}
.svc{position:absolute;width:300px;text-align:center}
.svc svg{display:block;margin:0 auto}
.svc h3{font-size:14px;font-weight:700;line-height:27px;text-transform:uppercase;margin-top:26px}
.svc p{font-size:13px;line-height:27px;margin-top:14px}

/* news */
.news{position:absolute;left:0;top:2709px;width:1200px;height:752px;background:var(--dark)}
.news-kicker{position:absolute;width:1200px;top:86px;text-align:center;font-size:14px;color:var(--gold-text)}
.news-title{position:absolute;width:1200px;top:118px;text-align:center;font-size:40px;font-weight:700}
.news-card{position:absolute;top:193px;width:317px;height:410px;background:var(--card);color:var(--ink)}
.news-img{position:absolute;left:5px;top:5px;width:307px;height:197px;background:linear-gradient(135deg,#c7cfd4,#7c8b92)}
.news-card h4{position:absolute;left:14px;top:230px;font-size:14px;font-weight:500;text-transform:uppercase}
.news-card p{position:absolute;left:14px;top:262px;width:292px;font-size:12.5px;line-height:23px;color:var(--muted)}
.news-meta{position:absolute;left:14px;top:377px;width:290px;font-size:12.5px;display:flex;align-items:center;gap:14px}
.news-meta .more{margin-left:auto;color:var(--gold);text-decoration:underline}
.slider-dots{position:absolute;left:544px;top:646px;display:flex;gap:9px}
.slider-dots span{width:14px;height:14px;border:1.5px solid #ddd;border-radius:50%}
.slider-dots span.on{border-color:var(--gold-text)}

/* faq */
.faq{position:absolute;left:0;top:3461px;width:1200px;height:473px;background:var(--gold)}
.faq-title{position:absolute;width:1200px;top:26px;text-align:center;font-size:40px;font-weight:700}
.faq-item{position:absolute;width:466px;height:61px;background:var(--cream);color:var(--ink)}
.faq-q{position:absolute;left:14px;top:22px;font-size:12px;font-weight:700;text-transform:uppercase}
.faq-icon{position:absolute;right:14px;top:21px;width:18px;height:18px;border-radius:50%;background:var(--ink);color:var(--cream);font-size:15px;line-height:18px;text-align:center;font-weight:700}
.faq-a{position:absolute;left:14px;top:52px;width:440px;font-size:12.5px;line-height:26px}

/* footer */
.site-footer{position:absolute;left:0;top:3934px;width:1200px;height:468px;background:var(--dark)}
.foot-h{position:absolute;top:78px;font-size:14px;font-weight:700;text-transform:uppercase}
.quick{position:absolute;left:129px;top:124px;font-size:15px;line-height:34px;list-style:none}
.contact-row{position:absolute;left:311px;display:flex;gap:14px;font-size:15px;line-height:28px}
.contact-row svg{flex:none;margin-top:6px}
.social{position:absolute;left:625px;display:flex;align-items:center;gap:8px;font-size:15px}
.social i{width:32px;height:32px;border:2px solid #fff;border-radius:50%}
.news-input{position:absolute;left:839px;top:130px;width:246px;height:41px;background:#fff;color:#888;font-size:13px;padding:12px}
.foot-line{position:absolute;left:111px;top:380px;width:978px;height:1px;background:#7a8782}
.copy{position:absolute;width:1200px;top:412px;text-align:center;font-size:14px}
</style>
</head>
<body>

<header class="site-header">
  <div class="brand">
    <div class="brand-mark"></div>
    <div>
      <div class="brand-name">Ferrando Quispe</div>
      <div class="brand-sub">ABOGADOS Y CONSULTORES</div>
    </div>
  </div>
  <nav class="main-nav">
    <a class="active">Home</a><a>About us</a><a>Services</a><a>How we work</a><a>Blog</a><a>FAQ</a><a>Contact</a>
  </nav>
</header>

<section class="hero">
  <div class="hero-photo" role="img" aria-label="Three smiling lawyers working together at a laptop in a wood-panelled office"></div>
  <div class="hero-dots"><span class="on"></span><span class="on"></span><span></span><span></span></div>
  <div class="hero-band"></div>
  <h1 class="hero-title">FERRANDO QUISPE</h1>
  <p class="hero-text">Lorem ipsum dolor sit amet, consectetur adipiscing elit, sed do eiusmod tempor incididunt ut labore et dolore magna</p>
  <a class="btn" style="left:807px;top:556px;width:278px;height:50px">Half hour free consultation</a>
</section>

<section class="about">
  <div class="about-bg" role="img" aria-label="Faint background photo of a businessman in glasses"></div>
  <div class="about-photo" role="img" aria-label="Lawyer reviewing documents with an older client at a desk"></div>
  <h2 class="sec-title" style="left:598px;top:150px">About us</h2>
  <p class="about-text">Lorem ipsum dolor sit amet, consectetur adipiscing elit, sed do eiusmod tempor incididunt ut labore et dolore magna aliqua. Ut enim ad minim veniam, quis nostrud exercitation ullamco laboris nisi ut aliquip ex ea commodo consequat. Duis aute irure dolor in reprehenderit in voluptate velit esse cillum dolore eu fugiat nulla pariatur. Excepteur sint occaecat cupidatat non proident, sunt in culpa qui officia deserunt mollit anim id est laborum</p>
  <a class="btn" style="left:600px;top:414px;width:364px;height:49px">Lawyer at your home for special cases</a>

  <h2 class="sec-title" style="left:0;width:1200px;text-align:center;top:616px">How we work</h2>
  <div class="work-card" style="left:111px;background:linear-gradient(160deg,#e9e6df,#b88a5e 60%,#6b4f38)" role="img" aria-label="Business team meeting around a conference table"></div>
  <div class="work-card" style="left:441px;background:linear-gradient(160deg,#8a7a6a,#d9cfc0 50%,#7b5e42)" role="img" aria-label="Hands reviewing plans on a desk with a hard hat"></div>
  <div class="work-card" style="left:771px;background:linear-gradient(160deg,#d4d6d8,#8fa2b8 50%,#5a6470)" role="img" aria-label="Tablet showing financial bar charts beside paper reports"></div>
  <div class="work-cap" style="left:111px">Bankruptcy and reorganization<br>of companies</div>
  <div class="work-cap" style="left:441px">Judicial defense in civil<br>matters</div>
  <div class="work-cap" style="left:771px">Financial and tax advice</div>
</section>

<section class="services">
  <h2 style="position:absolute;width:1200px;top:44px;text-align:center;font-size:40px;font-weight:700">SERVICES</h2>

  <div class="svc" style="left:110px;top:134px">
    <svg width="64" height="64" viewBox="0 0 64 64" fill="none" stroke="#fff" stroke-width="2"><path d="M12 6h30l8 8v22"/><path d="M12 6v52h26"/><path d="M18 18h22M18 26h26M18 34h20M18 42h12"/><path d="M48 38l10 4v8c0 6-5 9-10 11-5-2-10-5-10-11v-8z"/><path d="M44 50l3 3 6-6"/></svg>
    <h3>Commercial and corporate<br>law advisory</h3>
    <p>Lorem ipsum dolor sit amet, adipiscing elit, sed do eiusmod tempor incididunt ut labore et dolore magna aliqua. Ut enim ad</p>
  </div>
  <div class="svc" style="left:448px;top:134px">
    <svg width="64" height="64" viewBox="0 0 64 64" fill="none" stroke="#fff" stroke-width="2"><path d="M18 4h28v56H18z"/><path d="M24 14h16M24 20h16M24 44h16M24 50h10"/><circle cx="32" cy="32" r="6"/></svg>
    <h3>Legal defense in civil, criminal,<br>labor and family matters</h3>
    <p>Lorem ipsum dolor sit amet, adipiscing elit, sed do eiusmod tempor incididunt ut labore et dolore magna aliqua. Ut enim ad</p>
  </div>
  <div class="svc" style="left:785px;top:134px">
    <svg width="64" height="64" viewBox="0 0 64 64" fill="none" stroke="#fff" stroke-width="2"><path d="M6 8h52v12H6zM6 26h52v12H6zM6 44h52v12H6z"/><path d="M14 14h20M14 32h20M14 50h20"/></svg>
    <h3>Bankruptcy and reorganization<br>of companies</h3>
    <p>Lorem ipsum dolor sit amet, adipiscing elit, sed do eiusmod tempor incididunt ut labore et dolore magna aliqua. Ut enim ad</p>
  </div>
  <div class="svc" style="left:110px;top:415px">
    <svg width="64" height="64" viewBox="0 0 64 64" fill="none" stroke="#fff" stroke-width="2"><path d="M20 4h36v40H20z"/><circle cx="38" cy="16" r="6"/><path d="M35 16l2 2 4-4M26 28h24M26 34h18"/><path d="M4 60h40M10 60V46h24v14M14 52h16"/></svg>
    <h3>Collection and recovery of<br>assets</h3>
    <p>Lorem ipsum dolor sit amet, adipiscing elit, sed do eiusmod tempor incididunt ut labore et dolore magna aliqua. Ut enim ad</p>
  </div>
  <div class="svc" style="left:448px;top:415px">
    <svg width="64" height="64" viewBox="0 0 64 64" fill="none" stroke="#fff" stroke-width="2"><path d="M4 20L32 6l28 14z"/><path d="M8 24h48M8 52h48M4 58h56"/><path d="M14 28v20M24 28v20M34 28v20M44 28v20M52 28v20"/></svg>
    <h3>Asset protection</h3>
    <p>Lorem ipsum dolor sit amet, adipiscing elit, sed do eiusmod tempor incididunt ut labore et dolore magna aliqua. Ut enim ad</p>
  </div>
  <div class="svc" style="left:785px;top:415px">
    <svg width="64" height="64" viewBox="0 0 64 64" fill="none" stroke="#fff" stroke-width="2"><path d="M4 60h56"/><path d="M10 60V46h8v14M24 60V38h8v14M38 60V30h8v30"/><path d="M8 40l14-10 12 4 14-14"/><circle cx="52" cy="10" r="7"/></svg>
    <h3>Financial and tax advice</h3>
    <p>Lorem ipsum dolor sit amet, adipiscing elit, sed do eiusmod tempor incididunt ut labore et dolore magna aliqua. Ut enim ad</p>
  </div>

  <a class="btn" style="left:460px;top:689px;width:280px;height:51px">Monthly service packages</a>
</section>

<section class="news">
  <div class="news-kicker">LOREM IPSUM DOLOR</div>
  <h2 class="news-title">LATEST NEWS</h2>

  <article class="news-card" style="left:111px">
    <div class="news-img" role="img" aria-label="Hands reviewing financial charts on paper"></div>
    <h4>Lorem ipsum dolor sit amet</h4>
    <p>Sed ut perspiciatis unde omnis iste natus error sit voluptatem accusantium laudantium, totam rem aperiam, eaque ipsa quae</p>
    <div class="news-meta"><span>145 views</span><span>♡ 55</span><a class="more">READ MORE</a></div>
  </article>
  <article class="news-card" style="left:441px">
    <div class="news-img" role="img" aria-label="Business people at a meeting table with laptops" style="background:linear-gradient(135deg,#d8d2c8,#6e6258)"></div>
    <h4>Lorem ipsum dolor sit amet</h4>
    <p>Sed ut perspiciatis unde omnis iste natus error sit voluptatem accusantium laudantium, totam rem aperiam, eaque ipsa quae</p>
    <div class="news-meta"><span>145 views</span><span>♡ 55</span><a class="more">READ MORE</a></div>
  </article>
  <article class="news-card" style="left:771px">
    <div class="news-img" role="img" aria-label="Person working on a tablet at a desk with a calculator" style="background:linear-gradient(135deg,#b0a48e,#4e5560)"></div>
    <h4>Lorem ipsum dolor sit amet</h4>
    <p>Sed ut perspiciatis unde omnis iste natus error sit voluptatem accusantium laudantium, totam rem aperiam, eaque ipsa quae</p>
    <div class="news-meta"><span>145 views</span><span>♡ 55</span><a class="more">READ MORE</a></div>
  </article>

  <div class="slider-dots"><span></span><span></span><span class="on"></span><span></span><span></span></div>
</section>

<section class="faq">
  <h2 class="faq-title">FAQ</h2>
  <div class="faq-item" style="left:111px;top:109px"><span class="faq-q">Lorem ipsum dolor sit amet, consectetur ?</span><span class="faq-icon">+</span></div>
  <div class="faq-item" style="left:111px;top:194px"><span class="faq-q">Lorem ipsum dolor sit amet, consectetur ?</span><span class="faq-icon">+</span></div>
  <div class="faq-item" style="left:111px;top:280px"><span class="faq-q">Lorem ipsum dolor sit amet, consectetur ?</span><span class="faq-icon">+</span></div>
  <div class="faq-item" style="left:111px;top:365px"><span class="faq-q">Lorem ipsum dolor sit amet, consectetur ?</span><span class="faq-icon">+</span></div>

  <div class="faq-item" style="left:602px;top:109px"><span class="faq-q">Lorem ipsum dolor sit amet, consectetur ?</span><span class="faq-icon">+</span></div>
  <div class="faq-item" style="left:602px;top:194px;height:147px"><span class="faq-q">Lorem ipsum dolor sit amet, consectetur ?</span><span class="faq-icon">−</span>
    <p class="faq-a">Lorem ipsum dolor sit amet, consectetur adipiscing elit, sed do eiusmod tempor incididunt ut labore et dolore magna aliqua. Ut enim ad minim veniam, quis nostrud exercitation</p></div>
  <div class="faq-item" style="left:602px;top:365px"><span class="faq-q">Lorem ipsum dolor sit amet, consectetur ?</span><span class="faq-icon">+</span></div>
</section>

<footer class="site-footer">
  <div class="foot-h" style="left:126px">Quicklinks</div>
  <div class="foot-h" style="left:311px">Contact us</div>
  <div class="foot-h" style="left:629px">Connect with us</div>
  <div class="foot-h" style="left:839px">Newsletter</div>

  <ul class="quick"><li>Home</li><li>About us</li><li>Services</li><li>How we work</li><li>Blog</li><li>FAQ</li><li>Contact</li></ul>

  <div class="contact-row" style="top:119px">
    <svg width="16" height="16" viewBox="0 0 24 24" fill="none" stroke="#fff" stroke-width="1.8"><path d="M5 3h4l2 5-3 2a12 12 0 006 6l2-3 5 2v4a2 2 0 01-2 2A18 18 0 013 5a2 2 0 012-2z"/></svg>
    <span style="margin-left:6px">600-555-0142</span>
  </div>
  <div class="contact-row" style="top:163px">
    <svg width="16" height="18" viewBox="0 0 24 24" fill="#fff"><path d="M12 2a7 7 0 017 7c0 5-7 13-7 13S5 14 5 9a7 7 0 017-7zm0 4a3 3 0 100 6 3 3 0 000-6z"/></svg>
    <span>Lorem ipsum dolor sit amet,<br>consectetur adipiscing</span>
  </div>
  <div class="contact-row" style="top:236px">
    <svg width="16" height="14" viewBox="0 0 24 20" fill="none" stroke="#fff" stroke-width="1.8"><path d="M2 2h20v16H2z"/><path d="M2 2l10 9 10-9"/></svg>
    <span>info@ferrandoquispe.example</span>
  </div>

  <div class="social" style="top:124px"><i></i>Circlebook</div>
  <div class="social" style="top:164px"><i></i>Snapgallery</div>
  <div class="social" style="top:203px"><i></i>Chirper</div>
  <div class="social" style="top:241px"><i></i>Worknet</div>

  <div class="news-input">Enter Name</div>
  <a class="btn" style="left:839px;top:190px;width:137px;height:41px;font-size:14px">Subscribe</a>

  <div class="foot-line"></div>
  <div class="copy">copyrights © 2021 All Rights Reserved</div>
</footer>

</body>
</html>
```